Etiketten für biologisch und vegan produzierten Wein gesucht
Zielgruppe: anspruchsvolle Kunde, die biologisch und vegan produzierten Wein suchen. Sowie Fans des Hauspferdes Kolbi (s. dazu Homepage www.KOLBI.HOF)
Das Etikett für die Weinflasche soll ca. 20 cm lang und 10 cm hoch sein. Die Länge soll dreigeteilt sein, wobei alle Teile gleich groß sind. Der linke Teil wird Angaben zum Wein enthalten (Barcode, Zertifizierungen etc.), der rechte 'Lyrik/Beschreibung' zum Wein. Der Zentrale (mittlere) Teil wird auf der Flaschenvorderseite zu sehen sein. Hier soll das Logo (KOLBI.HOF) und die Worte: BIO VEGAN SÄUREARM zu sehen sein. Schriftfarbe wie Logofarbe: GOLD.
Zum Verständnis der Aufteilung des Etiketts, habe ich ein aktuelles Etikett beigefügt (in diesem Falle Weißwein). Der zentrale Anteil des Etiketts (Mitte) ist optisch völlig inakzeptabel (habe ich selbst gemacht).

```html
<!DOCTYPE html>
<html lang="de">
<head>
<meta charset="utf-8">
<title>KOLBI.HOF – Weinetikett</title>
<link rel="stylesheet" href="https://fonts.googleapis.com/css2?family=Open+Sans:wght@400;600&family=Oswald:wght@500;700&display=swap">
<style>
  :root {
    --backdrop: #e4e4e4;
    --label-paper: #fbfbf9;
    --gold: #b8932a;
    --gold-dark: #9a7a1f;
    --silhouette: #121212;
  }
  * { box-sizing: border-box; margin: 0; padding: 0; }
  html, body {
    width: 1200px;
    height: 924px;
    overflow: hidden;
    background: var(--backdrop);
  }
  .canvas {
    position: relative;
    width: 1200px;
    height: 924px;
  }
  .label {
    position: absolute;
    left: 237px;
    top: 50px;
    width: 725px;
    height: 825px;
    background: var(--label-paper);
    overflow: hidden;
  }
  .label__rule {
    position: absolute;
    left: 0;
    width: 100%;
    height: 14px;
  }
  .label__rule--top { top: 10px; }
  .label__rule--bottom { top: 795px; }
  .label__artwork {
    position: absolute;
    left: 25px;
    top: 40px;
    width: 225px;
    height: 700px;
    background: linear-gradient(180deg, #1c1c1c 0%, var(--silhouette) 100%);
    border-radius: 90px 60px 16px 16px;
  }
  .brand-name {
    position: absolute;
    left: 300px;
    top: 155px;
    width: 270px;
    text-align: center;
    font-family: "Open Sans", sans-serif;
    font-weight: 400;
    font-size: 44px;
    letter-spacing: 1px;
    color: var(--gold);
  }
  .claim {
    position: absolute;
    left: 268px;
    top: 520px;
    font-family: "Oswald", sans-serif;
    font-weight: 700;
    font-size: 22px;
    letter-spacing: 0.5px;
    color: var(--gold);
  }
  .volume {
    position: absolute;
    left: 282px;
    top: 748px;
    font-family: "Oswald", sans-serif;
    font-weight: 500;
    font-size: 22px;
    line-height: 1.3;
    color: var(--gold-dark);
    word-spacing: 8px;
  }
  .description {
    position: absolute;
    left: 652px;
    top: 70px;
    width: 64px;
    height: 700px;
  }
  .description__text {
    width: 64px;
    font-family: "Oswald", sans-serif;
    font-weight: 500;
    font-size: 10px;
    line-height: 1.7;
    color: var(--gold-dark);
  }
  .description__text p { margin-bottom: 22px; }
</style>
</head>
<body>
  <main class="canvas">
    <section class="label">
      <svg class="label__rule label__rule--top" viewBox="0 0 725 14" preserveAspectRatio="none">
        <path d="M0 4 L725 3" stroke="var(--gold)" stroke-width="3" fill="none"/>
        <path d="M0 11 L725 10" stroke="var(--gold)" stroke-width="1.5" fill="none"/>
      </svg>

      <div class="label__artwork" role="img" aria-label="Schwarze Silhouette eines schreitenden Pferdes"></div>

      <div class="brand-name">KOLBI.HOF</div>
      <div class="claim">BIO VEGAN SÄUREARM</div>
      <div class="volume">14% vol 750ml</div>

      <div class="description">
        <div class="description__text">
          <p>Die Trauben reifen langsam am sonnigen Südhang und werden von Hand gelesen.</p>
          <p>Dunkle Kirsche, reife Pflaume und ein Hauch Vanille tragen den Wein.</p>
          <p>Die milde Säure macht ihn bekömmlich und rund am Gaumen.</p>
          <p>Schön zu Pasta, Käse und Gemüse.</p>
        </div>
      </div>

      <svg class="label__rule label__rule--bottom" viewBox="0 0 725 14" preserveAspectRatio="none">
        <path d="M0 4 L725 4" stroke="var(--gold)" stroke-width="1.5" fill="none"/>
        <path d="M0 10 L725 11" stroke="var(--gold)" stroke-width="3" fill="none"/>
      </svg>
    </section>
  </main>
</body>
</html>
```